Business Card Design for Venture Lantern

Venture Lantern is a pro bono student consultancy service offered by Solvari KPTC to social start ups and enterprises. We provide consulting services with expertise in areas such as Marketing, IT, Business Strategy and Innovation.
I have attached\ the Venture Lantern Logo here for your perusal.
Industry/Entity Type
Business
Contact Information for Business Card
Name: Dae Hwan Park Name: Thomas Leung
Role: Project Leader Role: Vice Project Leader
M:0491203846 M: 0473560218
E: dae-hwan.park@solvarikptc.org E: thomas.leung@solvarikptc.org
W: www.solvarikptc.org W: www.solvarikptc.org

```html
<!DOCTYPE html>
<html lang="en">
<head>
<meta charset="utf-8">
<title>Venture Lantern — Business Cards</title>
<link rel="stylesheet" href="https://fonts.googleapis.com/css2?family=Oswald:wght@700&family=Arimo:wght@400&display=swap">
<style>
  :root {
    --page-bg: #e6e6e8;
    --card-white: #fbfdfd;
    --card-dark: #33333d;
    --ink: #1c1c1c;
    --orange: #f0a030;
    --yellow: #f5c21b;
    --divider: #2a2a2a;
  }
  * { box-sizing: border-box; margin: 0; padding: 0; }
  html, body {
    width: 1200px; height: 960px; overflow: hidden;
    background: var(--page-bg);
  }
  .sheet {
    width: 1200px; height: 960px;
    display: flex; flex-direction: column; align-items: center; justify-content: center;
    gap: 60px;
  }
  .card {
    position: relative;
    width: 700px; height: 400px;
    box-shadow: 0 6px 18px rgba(0,0,0,0.18);
  }
  .card--front { background: var(--card-white); }
  .card--back {
    background: var(--card-dark);
    display: flex; align-items: center; justify-content: center;
  }

  .brand {
    font-family: "Oswald", sans-serif;
    font-weight: 700;
    text-transform: uppercase;
    line-height: 0.95;
  }
  .card--front .brand {
    position: absolute; left: 40px; top: 88px;
    font-size: 34px; color: var(--ink);
  }
  .card--back .brand {
    font-size: 66px; color: var(--yellow); text-align: center;
  }

  .accent-rule {
    position: absolute; left: 230px; top: 126px;
    width: 430px; height: 2px; background: var(--orange);
  }
  .website {
    position: absolute; right: 40px; top: 96px;
    font-family: "Arimo", sans-serif; font-size: 17px; color: var(--ink);
  }

  .contacts {
    position: absolute; left: 232px; top: 218px;
    display: flex; align-items: stretch;
  }
  .contact { width: 220px; font-family: "Arimo", sans-serif; color: var(--ink); }
  .contact + .contact { padding-left: 22px; }
  .contact-divider { width: 1.5px; background: var(--divider); margin-left: 4px; }
  .contact__name { color: var(--orange); font-size: 23px; line-height: 1.1; }
  .contact__role { font-size: 14px; margin-top: 4px; }
  .contact__lines { margin-top: 26px; display: grid; gap: 8px; }
  .contact__line { display: flex; align-items: center; gap: 8px; font-size: 13px; white-space: nowrap; }
  .contact__line svg { flex: none; }
</style>
</head>
<body>
<main class="sheet">
  <section class="card card--front" aria-label="Business card front">
    <div class="brand">Venture<br>Lantern</div>
    <div class="website">www.solvarikptc.org</div>
    <div class="accent-rule"></div>

    <div class="contacts">
      <div class="contact">
        <div class="contact__name">Dae Hwan Park</div>
        <div class="contact__role">Project Leader</div>
        <div class="contact__lines">
          <div class="contact__line">
            <svg width="10" height="14" viewBox="0 0 10 14"><rect x="1" y="0.5" width="8" height="13" rx="1.5" fill="none" stroke="#1c1c1c"/><rect x="2.5" y="2.5" width="5" height="7" fill="#1c1c1c"/></svg>
            <span>0491203846</span>
          </div>
          <div class="contact__line">
            <svg width="12" height="10" viewBox="0 0 12 10"><rect x="0.5" y="0.5" width="11" height="9" rx="1" fill="#1c1c1c"/><path d="M1 1.5 L6 5.5 L11 1.5" fill="none" stroke="#fff" stroke-width="1"/></svg>
            <span>dae-hwan.park@solvarikptc.org</span>
          </div>
        </div>
      </div>
      <div class="contact-divider"></div>
      <div class="contact">
        <div class="contact__name">Thomas Leung</div>
        <div class="contact__role">Vice Project Leader</div>
        <div class="contact__lines">
          <div class="contact__line">
            <svg width="10" height="14" viewBox="0 0 10 14"><rect x="1" y="0.5" width="8" height="13" rx="1.5" fill="none" stroke="#1c1c1c"/><rect x="2.5" y="2.5" width="5" height="7" fill="#1c1c1c"/></svg>
            <span>0473560218</span>
          </div>
          <div class="contact__line">
            <svg width="12" height="10" viewBox="0 0 12 10"><rect x="0.5" y="0.5" width="11" height="9" rx="1" fill="#1c1c1c"/><path d="M1 1.5 L6 5.5 L11 1.5" fill="none" stroke="#fff" stroke-width="1"/></svg>
            <span>thomas.leung@solvarikptc.org</span>
          </div>
        </div>
      </div>
    </div>
  </section>

  <section class="card card--back" aria-label="Business card back">
    <div class="brand">Venture<br>Lantern</div>
  </section>
</main>
</body>
</html>
```